Pictures required on web page

I would like change three existing pictures on my new website.

The site can be found here:
http://mossbottleroom.kestrelweb.com.au/

The three pictures to be changed are on the home page:
Purchase- Mixed Packs
Wine Club - Let Us Choose
Education- Wine Courses

I would like somthing stylish, classic and understated that fits in with the theme and feel of the site. I know stylish is a subjective thing. At the moment, the current picture makes the text difficult to read on a destop. Plus I don't think they are a perfect fit for our website anyway. I've attached a photo of our wine course room and also me in the store. Please, don't feel as though you have to use these pictures, but they're there if you want them. However I'm open to completely different photos/graphics to be used.

```html
<!DOCTYPE html>
<html lang="en">
<head>
<meta charset="utf-8">
<title>Mossbottle – Small winery specialist</title>
<link rel="stylesheet" href="https://fonts.googleapis.com/css2?family=Roboto+Slab:wght@500&family=Roboto:wght@400;500&family=Open+Sans:wght@400;600;700&family=Raleway:wght@500&family=Great+Vibes&display=swap">
<style>
:root{
  --navy:#263a63;
  --navy-deep:#1c2b4c;
  --nav-bar:#161f33;
  --gold-a:#c9a23a;
  --gold-b:#e2c25a;
  --label-dark:#1f2d4d;
  --red:#b5494a;
  --card-navy:#22335a;
  --white:#ffffff;
  --ink:#1d1d1d;
}
*{box-sizing:border-box;margin:0;padding:0}
html,body{width:1200px;height:662px;overflow:hidden;background:var(--white)}
body{position:relative;font-family:"Open Sans",sans-serif}

.site-header{position:absolute;left:0;top:0;width:1200px;height:95px;
  background:linear-gradient(180deg,var(--navy) 0%,var(--navy-deep) 100%)}
.brand{position:absolute;left:160px;top:18px;color:var(--white)}
.brand-name{font-family:"Roboto Slab",serif;font-weight:500;font-size:33px;line-height:36px;letter-spacing:.3px}
.brand-tagline{font-family:"Roboto Slab",serif;font-weight:500;font-size:15px;line-height:16px;color:#d6dbe6;opacity:.9}
.search{position:absolute;left:410px;top:31px;width:258px;height:30px;border:1px solid #5b6f98;
  border-radius:3px;background:#334a78;color:#a9b6cf;font-family:"Roboto",sans-serif;font-size:13px;
  padding:7px 11px}
.search svg{position:absolute;right:8px;top:4px}
.utility{position:absolute;left:695px;top:26px;display:flex}
.utility a{display:flex;flex-direction:column;align-items:center;gap:6px;color:#d9deea;text-decoration:none;
  font-family:"Roboto",sans-serif;font-size:10.5px;letter-spacing:.3px;padding:0 13px;border-right:1px solid #3d5078;height:40px}
.utility a:last-child{border-right:none}

.main-nav{position:absolute;left:0;top:95px;width:1200px;height:42px;background:var(--nav-bar)}
.main-nav ul{list-style:none;position:absolute;left:161px;top:11px;display:flex;gap:26px}
.main-nav li{color:var(--white);font-family:"Roboto",sans-serif;font-size:16px}
.cart{position:absolute;left:906px;top:12px;display:flex;gap:8px;align-items:center;color:#e3e6ee;
  font-family:"Roboto",sans-serif;font-size:11.5px}

.tile{position:absolute;overflow:hidden}
.tile-photo{position:absolute;left:0;top:0;width:100%}
.tile-label{position:absolute;left:0;width:100%;height:42px;display:flex}
.label-script{width:120px;background:var(--label-dark);color:var(--white);font-family:"Great Vibes",cursive;
  font-size:25px;display:flex;align-items:center;justify-content:center}
.label-title{flex:1;background:linear-gradient(90deg,var(--gold-a),var(--gold-b));color:#20253a;
  font-family:"Raleway",sans-serif;font-weight:500;font-size:18px;letter-spacing:.4px;display:flex;align-items:center;padding-left:10px}

.tile-courses{left:144px;top:150px;width:291px;height:196px}
.tile-courses .tile-photo{height:154px;background:radial-gradient(circle at 60% 40%,#8f6a3a 0%,#4a2a14 55%,#140806 100%)}
.tile-courses .tile-label{top:154px}

.tile-club{left:454px;top:150px;width:292px;height:338px;background:#1c1c1c}
.tile-club .tile-photo{height:263px;background:linear-gradient(180deg,#a97a4c 0%,#c89a6a 40%,#6d4a2c 80%,#2a2119 100%)}
.tile-club .tile-label{top:221px}
.tile-club .label-script{width:120px}
.read-more{position:absolute;left:95px;top:280px;width:101px;height:33px;border:2px solid var(--white);
  outline:1px solid #999;outline-offset:1px;color:var(--white);font-weight:700;font-size:13px;
  display:flex;align-items:center;justify-content:center;background:#151515}

.tile-packs{left:764px;top:150px;width:291px;height:196px}
.tile-packs .tile-photo{height:154px;background:radial-gradient(circle at 45% 35%,#f08a2a 0%,#c24e0c 50%,#5a1c05 100%)}
.tile-packs .tile-label{top:154px}

.promo{position:absolute;width:291px;height:131px;top:357px;color:var(--white);text-align:center}
.promo::before{content:"";position:absolute;inset:7px;border:3px double var(--white)}
.promo h2{font-weight:700;font-size:23px;margin-top:35px;letter-spacing:.3px}
.promo p{font-size:13px;display:inline-block;border-top:1px dotted rgba(255,255,255,.7);padding-top:1px;margin-top:1px}
.promo-shipping{left:144px;background:var(--red)}
.promo-newsletter{left:764px;background:var(--card-navy)}

.product{position:absolute}
.product-red{left:221px;top:526px;width:60px;height:136px;border-radius:10px 10px 0 0;
  background:linear-gradient(180deg,#b8763a 0%,#8c5424 20%,#1a1210 22%,#2a1a16 100%)}
.product-white{left:457px;top:522px;width:52px;height:140px;border-radius:10px 10px 0 0;
  background:linear-gradient(180deg,#111 0%,#222 20%,#5c5b2e 24%,#7d7a3e 100%)}
</style>
</head>
<body>
<header class="site-header">
  <div class="brand">
    <div class="brand-name">Mossbottle</div>
    <div class="brand-tagline">Small winery specialist.</div>
  </div>
  <div class="search">Search the Cellars
    <svg width="22" height="22" viewBox="0 0 22 22"><circle cx="9" cy="9" r="6.5" fill="none" stroke="#dfe4ee" stroke-width="2"/><line x1="13.8" y1="13.8" x2="20" y2="20" stroke="#dfe4ee" stroke-width="2.6" stroke-linecap="round"/></svg>
  </div>
  <nav class="utility">
    <a href="#"><svg width="14" height="13" viewBox="0 0 14 13"><path d="M7 0 0 6h2v7h4V9h2v4h4V6h2z" fill="#dfe4ee"/></svg>HOME</a>
    <a href="#"><svg width="20" height="14" viewBox="0 0 20 14"><circle cx="10" cy="4" r="3.2" fill="#dfe4ee"/><circle cx="4" cy="5" r="2.4" fill="#dfe4ee"/><circle cx="16" cy="5" r="2.4" fill="#dfe4ee"/><path d="M4 14c0-4 2.5-6 6-6s6 2 6 6z" fill="#dfe4ee"/><path d="M0 13c0-3 1.5-5 4-5 1 0 1.6.3 2 .6C4.5 10 4 11.5 4 13z M20 13c0-3-1.5-5-4-5-1 0-1.6.3-2 .6 1.5 1.4 2 2.9 2 4.4z" fill="#dfe4ee"/></svg>ABOUT</a>
    <a href="#"><svg width="14" height="14" viewBox="0 0 14 14"><rect x="1" y="2" width="12" height="11" rx="1" fill="none" stroke="#dfe4ee" stroke-width="1.6"/><rect x="1" y="2" width="12" height="3" fill="#dfe4ee"/><rect x="3.5" y="0" width="1.6" height="3" fill="#dfe4ee"/><rect x="9" y="0" width="1.6" height="3" fill="#dfe4ee"/></svg>EVENTS</a>
    <a href="#"><svg width="14" height="14" viewBox="0 0 14 14"><circle cx="7" cy="7" r="4.2" fill="none" stroke="#dfe4ee" stroke-width="2.6" stroke-dasharray="2.2 1.1"/><circle cx="7" cy="7" r="3" fill="none" stroke="#dfe4ee" stroke-width="1.6"/></svg>ACCOUNT</a>
    <a href="#"><svg width="13" height="13" viewBox="0 0 13 13"><path d="M2.5 0.5 5 3 3.6 4.6c.8 1.9 2.4 3.5 4.3 4.3L9.5 7.5 12 10l-1.6 2.2C5.5 12 1 7.5.8 2.1z" fill="#dfe4ee"/></svg>CONTACT</a>
  </nav>
</header>

<nav class="main-nav">
  <ul>
    <li>Red Wine</li><li>White Wine</li><li>Sparkling</li><li>Rosé</li><li>Old &amp; Rare</li><li>Stickies</li><li>Imported</li><li>Wine Club</li>
  </ul>
  <div class="cart">
    <svg width="22" height="18" viewBox="0 0 22 18"><path d="M0 1h4l3 10h11l3-8H6" fill="none" stroke="#fff" stroke-width="2"/><path d="M6 3h15l-3 8H7z" fill="#fff"/><circle cx="8.5" cy="15.5" r="1.8" fill="#fff"/><circle cx="17" cy="15.5" r="1.8" fill="#fff"/></svg>
    Shopping cart is empty
  </div>
</nav>

<main>
  <section class="tile tile-courses">
    <div class="tile-photo" role="img" aria-label="Photo of a glass of red wine on an oak barrel with grapes and vine leaves"></div>
    <div class="tile-label"><span class="label-script">Education</span><span class="label-title">WINE COURSES</span></div>
  </section>

  <section class="tile tile-club">
    <div class="tile-photo" role="img" aria-label="Photo of rows of oak wine barrels stacked in a cellar"></div>
    <div class="tile-label"><span class="label-script">Wine Club</span><span class="label-title">LET US CHOOSE</span></div>
    <a class="read-more">Read More</a>
  </section>

  <section class="tile tile-packs">
    <div class="tile-photo" role="img" aria-label="Photo of red and white wine glasses with bottles and grapes on a warm orange backdrop"></div>
    <div class="tile-label"><span class="label-script">Purchase</span><span class="label-title">MIXED PACKS</span></div>
  </section>

  <section class="promo promo-shipping">
    <h2>FREE SHIPPING</h2>
    <p>On order over $200</p>
  </section>

  <section class="promo promo-newsletter">
    <h2>NEWSLETTER</h2>
    <p>Join the newsletter for specials</p>
  </section>

  <div class="product product-red" role="img" aria-label="Product photo of a red wine bottle with copper capsule"></div>
  <div class="product product-white" role="img" aria-label="Product photo of a white wine bottle with black screw cap"></div>
</main>
</body>
</html>
```